Membership Comparison Chart

I need the current membership chart recreated with additional perks listed at the bottom with our other companies, when you purchase a membership with us. Please remove the "curated cafe" at the bottom (has not opened yet). We are a shooting range and education center. This chart was originally created 2 years ago. I need in file form that is printable as well as a file that is able to be updated periodically. Please add the words "A Marbisk Group Company" below the logo attached.

```html
<!DOCTYPE html>
<html lang="en">
<head>
<meta charset="utf-8">
<title>Membership Comparison Chart</title>
<link href="https://fonts.googleapis.com/css2?family=Inter:wght@400;600;700;800&family=Oswald:wght@700&display=swap" rel="stylesheet">
<style>
  :root{
    --ink:#2b2b2b;
    --muted:#5e5e5e;
    --red:#b5161c;
    --head:#262626;
    --elite:#3e72db;
    --plat:#8fc46f;
    --label-bg:#efefef;
    --rule:#a9a9a9;
    --tick:#4d5d6c;
    --paper:#ffffff;
  }
  *{box-sizing:border-box;margin:0;padding:0}
  html,body{width:927px;height:1200px;overflow:hidden;background:var(--paper)}
  body{font-family:"Inter",sans-serif;color:var(--ink);position:relative}

  .intro{text-align:center;padding-top:22px}
  .intro .kicker{font-weight:700;font-size:17px;letter-spacing:.3px}
  .intro .headline{font-family:"Oswald",sans-serif;font-weight:700;color:var(--red);font-size:37px;line-height:1.15;letter-spacing:.2px;margin-top:3px}
  .intro .sub{font-weight:700;font-size:17px;margin-top:4px}
  .intro .tagline{font-size:17px;margin-top:2px;color:#333}

  .chart{position:absolute;left:33px;top:154px;width:857px;display:grid;
    grid-template-columns:270px 196px 196px 195px;
    grid-template-rows:78px 63px 46px 45px 50px 48px 46px 49px 49px 65px 48px 49px 49px 33px 49px 83px;
    border-bottom:2px solid var(--rule)}
  .chart > div{border-bottom:1.5px solid var(--rule);border-left:1.5px solid #c9c9c9}
  .chart > .label{border-left:none}
  .head{background:var(--head);color:#fff;text-align:center;display:flex;flex-direction:column;justify-content:center;border-left:2px solid #9a9a9a!important;border-bottom:3px solid #777!important}
  .head.brand{border-left:none!important;flex-direction:row;align-items:center;justify-content:center;gap:9px}
  .brand .dot{width:40px;height:40px;border-radius:50%;background:#fff;flex:none}
  .brand .text{text-align:left}
  .brand .name{font-size:16px;font-weight:600;line-height:1.1;text-transform:uppercase;letter-spacing:.2px}
  .brand .institute{font-size:9.5px;font-weight:600;color:#e0262d;text-transform:uppercase;letter-spacing:.3px;margin-top:2px}
  .brand .group{font-size:10px;font-weight:400;color:#fff;letter-spacing:.3px;margin-top:2px}
  .tier{font-weight:800;font-size:22px;letter-spacing:.3px;line-height:1.1}
  .tier.elite{color:var(--elite)}
  .tier.plat{color:var(--plat)}
  .tier-sub{font-size:16px;letter-spacing:.5px;margin-top:2px}

  .label{background:var(--label-bg);padding:7px 6px 0 6px;font-size:14.5px;font-weight:700;line-height:1.22}
  .label small{display:block;font-weight:400;font-size:12.3px;color:var(--muted);line-height:1.3}
  .label small.dark{color:var(--ink)}
  .val{display:flex;flex-direction:column;justify-content:center;align-items:center;text-align:center;font-weight:700;font-size:16px;line-height:1.15}
  .val span{font-weight:400;font-size:13px;color:var(--muted);letter-spacing:.3px}
  .val span.dark{color:var(--ink)}
  .val span.sm{font-weight:700;color:var(--ink);font-size:14.5px}
  .val sup{font-size:9px;vertical-align:6px}
  .val .tick{width:20px;height:20px}

  .extras-title{position:absolute;left:33px;top:1010px;font-size:20px;font-weight:700}
  .perks{position:absolute;left:37px;top:1039px;width:852px;height:119px;display:grid;grid-template-columns:210px 210px 210px 210px;gap:0 4px}
  .stack{display:grid;grid-template-rows:1fr 1fr;gap:4px}
  .perk{border:2.5px solid #222;background:#fff;display:flex;align-items:center;gap:6px;padding:3px 5px;text-align:center;font-weight:800;font-size:10.5px;line-height:1.15;text-transform:uppercase}
  .perk .note{font-weight:400}
  .perk .copy{flex:1}
  .badge{flex:none;width:46px;height:46px;border-radius:50%;background:#2a2a2a}
  .badge.light{background:#fff;border:1px solid #888}
  .perk.tall{flex-direction:column;justify-content:center;gap:4px}
  .perk .co{font-size:14px;font-weight:800;display:flex;align-items:center;gap:5px;justify-content:center}
  .perk .co i{display:block;width:26px;height:26px;background:#6cbf3c;border-radius:50%}
  .perk .co.red{color:var(--red);font-size:15px;line-height:1.1}
  .perk .lease{font-size:11.5px}
  .promise{font-weight:400;text-transform:none;font-size:10.4px;line-height:1.2}
  .promise-brand{display:flex;align-items:center;gap:5px;font-weight:700;font-size:9px;text-transform:uppercase;text-align:left}
  .promise-brand i{display:block;width:18px;height:18px;border-radius:50%;background:var(--red);flex:none}
  .promise-title{font-size:16px;font-weight:800}
</style>
</head>
<body>
  <header class="intro">
    <div class="kicker">FEATURING</div>
    <div class="headline">THE WORLD'S LARGEST INDOOR DOUBLE-DECK GUN RANGE,</div>
    <div class="sub">Digital Assault Survival Theater, and 20+ Safety-Focused Classes,</div>
    <div class="tagline">our membership gives you unbeatable value...</div>
  </header>

  <section class="chart">
    <div class="head brand">
      <span class="dot"></span>
      <div class="text">
        <div class="name">Ridgeline Armory<br>Shooting Center</div>
        <div class="institute">Firearm Safety Learning Institute</div>
        <div class="group">A Marbisk Group Company</div>
      </div>
    </div>
    <div class="head"><div class="tier">BASIC</div><div class="tier-sub">MEMBERSHIP</div></div>
    <div class="head"><div class="tier elite">ELITE</div><div class="tier-sub">MEMBERSHIP</div></div>
    <div class="head"><div class="tier plat">PLATINUM</div><div class="tier-sub">MEMBERSHIP</div></div>

    <div class="label">Family Gun &amp; Archery Range Use<small>You, your spouse and all children under 18.<br>Liberty Salute Range and Archery Range</small></div>
    <div class="val">FREE<span>UNLIMITED USE</span></div>
    <div class="val">FREE<span>UNLIMITED USE</span></div>
    <div class="val">FREE<span>UNLIMITED USE</span></div>

    <div class="label">FREE Firearm Lesson Level<small class="dark">tailored to your experience</small></div>
    <div class="val"></div>
    <div class="val">FREE LESSON</div>
    <div class="val">FREE LESSON</div>

    <div class="label">FREE Archery Lesson Level<small class="dark">tailored to your experience</small></div>
    <div class="val"></div>
    <div class="val">FREE LESSON</div>
    <div class="val">FREE LESSON</div>

    <div class="label">5% OFF All Firearms</div>
    <div class="val"></div>
    <div class="val"><span class="sm">STOCK AND<br>SPECIAL ORDER</span></div>
    <div class="val"><span class="sm">STOCK AND<br>SPECIAL ORDER</span></div>

    <div class="label">Digital Assault Survival and Fun Target Theaters</div>
    <div class="val">25% OFF</div>
    <div class="val">50% OFF</div>
    <div class="val">FREE 12 HOURS</div>

    <div class="label">10% OFF Everything Else<small>(Ammo, Holsters, Targets, Gun Bags, etc.)</small></div>
    <div class="val">10% OFF</div>
    <div class="val">10% OFF</div>
    <div class="val">10% OFF</div>

    <div class="label">Required Master Lane Target</div>
    <div class="val">10% OFF</div>
    <div class="val">10% OFF</div>
    <div class="val">1 FREE<span>EVERY VISIT</span></div>

    <div class="label">Discounts on RASC Training*<small>Dozens of Basic and Advanced Classes</small></div>
    <div class="val">25% OFF</div>
    <div class="val">50%OFF<span>PLUS 2 FREE REPEATS</span></div>
    <div class="val">1 FREE/VISIT<span>PLUS 10 FREE REPEATS</span></div>

    <div class="label">Free Guest Passes Per Year Sharing Lane With member</div>
    <div class="val">5 FREE<span>YEARLY</span></div>
    <div class="val">10 FREE<span>YEARLY</span></div>
    <div class="val">1 FREE / VISIT<span>PLUS 10 FREE FOR<br>GIFTING*</span></div>

    <div class="label">Gun Rentals</div>
    <div class="val">50% OFF</div>
    <div class="val">FREE</div>
    <div class="val">FREE<span>FOR MEMBER &amp; GUEST</span></div>

    <div class="label">Discount on FFL Transfer</div>
    <div class="val"><div><sup>$</sup>10 OFF</div></div>
    <div class="val"><div><sup>$</sup>15 OFF</div></div>
    <div class="val">FREE<span>UNLIMITED</span></div>

    <div class="label">NO Credit Card Hold for Lanes Firearm Deposit Required</div>
    <div class="val"><svg class="tick" viewBox="0 0 20 20"><path d="M2 10 L8 17 L18 2" fill="none" stroke="#4d5d6c" stroke-width="3" stroke-linecap="round" stroke-linejoin="round"/></svg></div>
    <div class="val"><svg class="tick" viewBox="0 0 20 20"><path d="M2 10 L8 17 L18 2" fill="none" stroke="#4d5d6c" stroke-width="3" stroke-linecap="round" stroke-linejoin="round"/></svg></div>
    <div class="val"><svg class="tick" viewBox="0 0 20 20"><path d="M2 10 L8 17 L18 2" fill="none" stroke="#4d5d6c" stroke-width="3" stroke-linecap="round" stroke-linejoin="round"/></svg></div>

    <div class="label">Free Meeting/Party Room</div>
    <div class="val">1 hr</div>
    <div class="val">5 hrs</div>
    <div class="val">10 HRS</div>

    <div class="label">Refer New Member Reward</div>
    <div class="val"><div><sup>$</sup>10</div><span>GIFT CARD</span></div>
    <div class="val"><div><sup>$</sup>20</div><span>GIFT CARD</span></div>
    <div class="val">$25<span>GIFT CARD</span></div>

    <div class="label">COST Plus 1-time $100 Initiation Fee<small>(No Fee if Paid in Full with Cash)</small></div>
    <div class="val"><div><sup>$</sup>35/MONTH</div><span>$520 TOTAL</span><div>SINGLE PAYMENT</div><span>$420 TOTAL</span></div>
    <div class="val"><div><sup>$</sup>55/MONTH</div><span class="dark">$760 TOTAL</span><div>SINGLE PAYMENT</div><span class="dark">$660 TOTAL</span></div>
    <div class="val"><div><sup>$</sup>79 /MONTH</div><span class="dark">$1048 TOTAL</span><div>SINGLE PAYMENT</div><span class="dark">$948 TOTAL</span></div>
  </section>

  <div class="extras-title">...plus these extra benefits you never expected.</div>

  <section class="perks">
    <div class="stack">
      <div class="perk"><span class="badge"></span><div class="copy">5 free outdoor indoor court passes<br><span class="note">(punch card)</span></div></div>
      <div class="perk"><span class="badge light"></span><div class="copy">5% off social events and wedding packages<br><span class="note">(venue rental)</span></div></div>
    </div>
    <div class="perk tall">
      <div class="co"><i></i>VERDANT YARD CO.</div>
      <div>50% off delivery fee for mulch, stone, topsoil.</div>
      <div>5% off concrete, basement waterproofing, snow mitigation, or lawn care</div>
    </div>
    <div class="perk tall">
      <div class="co red">NORTHGATE INDUSTRIAL<br>TECH CENTER</div>
      <div class="lease">10% off first month payment with a 1-year lease</div>
    </div>
    <div class="perk tall">
      <div class="promise-brand"><i></i>Ridgeline Armory Shooting Center</div>
      <div class="promise-title">OUR PROMISE</div>
      <div class="promise">We will do everything in our power to support our members' wellness health, and safety with education and training in a state-of-the-art facility.</div>
    </div>
  </section>
</body>
</html>
```